SEO AND WEB DESIGN COMPANY BUSINESS CARD DESIGN

I need an eye catching , simple business card design that will match my logo . I need 2 versions of it ( white background and black background) - SOME PEOPLE DID NOT GET IT AND SENDING US FRONT WHITE BACK WHITE VERSIONS WHICH IS NOT CORRECT.

ONE VERSION SHOULD BE BACK AND FRONT ALL BLACK , SECOND VERSION SHOULD BE BACK AND FRONT ALL WHITE

logo psd files are attached for both versions. The business card is going to have : First Name- Last name - position - phone numbers

```html
<!DOCTYPE html>
<html lang="en">
<head>
<meta charset="utf-8">
<title>Brightpath Digital — Business Card</title>
<link href="https://fonts.googleapis.com/css2?family=Oswald:wght@500;600&family=Work+Sans:wght@400;500&display=swap" rel="stylesheet">
<style>
  :root {
    --stage: #161616;
    --card: #232323;
    --card-edge: #2b2b2b;
    --accent: #4a86d0;
    --ink: #f2f2f2;
  }
  html, body {
    margin: 0;
    width: 1200px;
    height: 900px;
    overflow: hidden;
    background: var(--stage);
  }
  .canvas {
    width: 1200px;
    height: 900px;
    display: flex;
    flex-direction: column;
    align-items: center;
    justify-content: center;
    gap: 40px;
  }
  .card {
    position: relative;
    width: 660px;
    height: 377px;
    background: linear-gradient(135deg, var(--card) 0%, var(--card-edge) 100%);
    border-bottom: 4px solid var(--accent);
    box-sizing: border-box;
    font-family: "Work Sans", sans-serif;
    color: var(--ink);
  }
  /* Front */
  .card--front {
    display: flex;
    align-items: center;
    justify-content: center;
  }
  .brand {
    display: flex;
    align-items: center;
    gap: 16px;
  }
  .brand__dot {
    width: 34px;
    height: 34px;
    border-radius: 50%;
    background: var(--accent);
  }
  .brand__name {
    font-family: "Oswald", sans-serif;
    font-weight: 600;
    font-size: 54px;
    letter-spacing: 1px;
    text-transform: uppercase;
    color: var(--ink);
  }
  /* Back */
  .card--back .identity {
    position: absolute;
    right: 360px;
    top: 130px;
    text-align: right;
  }
  .identity__name {
    font-family: "Oswald", sans-serif;
    font-weight: 500;
    font-size: 38px;
    line-height: 1;
    text-transform: uppercase;
    color: var(--accent);
    white-space: nowrap;
    margin: 0;
  }
  .identity__role {
    font-size: 19px;
    margin: 8px 0 0;
    letter-spacing: 0.5px;
  }
  .divider {
    position: absolute;
    left: 318px;
    top: 128px;
    width: 2px;
    height: 70px;
    background: var(--accent);
  }
  .contact {
    position: absolute;
    left: 340px;
    top: 132px;
    margin: 0;
    padding: 0;
    list-style: none;
    font-size: 17px;
    line-height: 22px;
  }
  .contact li {
    display: flex;
    align-items: center;
    gap: 9px;
  }
  .contact svg {
    width: 13px;
    height: 13px;
    flex: none;
  }
  .address {
    position: absolute;
    left: 40px;
    bottom: 26px;
    margin: 0;
    font-size: 18px;
    letter-spacing: 0.5px;
  }
</style>
</head>
<body>
<main class="canvas">
  <section class="card card--front" aria-label="Card front">
    <div class="brand">
      <span class="brand__dot"></span>
      <span class="brand__name">Brightpath Digital</span>
    </div>
  </section>

  <section class="card card--back" aria-label="Card back">
    <div class="identity">
      <h1 class="identity__name">Daniel Reyes</h1>
      <p class="identity__role">Director</p>
    </div>
    <span class="divider"></span>
    <ul class="contact">
      <li>
        <svg viewBox="0 0 16 16" fill="none" stroke="#4a86d0" stroke-width="1.6"><path d="M4 1.5l2.5 3-1.5 1.5c.8 2 2.5 3.7 4.5 4.5L11 9l3 2.5-1.5 2.5C7 14 2 9 1.5 3.5z"/></svg>
        +1 555-014-2280
      </li>
      <li>
        <svg viewBox="0 0 16 16" fill="none" stroke="#4a86d0" stroke-width="1.6"><rect x="1.5" y="3.5" width="13" height="9"/><path d="M1.5 3.5l6.5 5 6.5-5"/></svg>
        hello@brightpath.com
      </li>
      <li>
        <svg viewBox="0 0 16 16" fill="none" stroke="#4a86d0" stroke-width="1.4"><circle cx="8" cy="8" r="6.5"/><ellipse cx="8" cy="8" rx="3" ry="6.5"/><path d="M1.5 8h13"/></svg>
        www.brightpath.com
      </li>
    </ul>
    <p class="address">1420 Harbor Lane Riverton, TX 75001</p>
  </section>
</main>
</body>
</html>
```